OK!REELS WEBSITE

I need to get the design for the website of my company, which is a production company based in Los Angeles called OK! REELS. The company works as a liason between Russian speaking and English speaking film communities, providing the spectrum of production services in Eastern Europe and United States of America.
Has to have the following links:
About
Locations
Works
I'd like to see the designs on the white background using the blue and red colors.
Please try to use the font of an old typewriter if you can. You can also get some ideas after looking at the logo, which you need to intergrate into the webdesign anyway.
Thank you very much and I wish you some inspiration!
Updates

I'd like to extend the project till July the 10th, please send more submissions

Reason: I want to give more time to make changes to my comments

Target Market(s)

Production studios from different countries, Directors, Producers, Clients

Industry/Entity Type

It Company

Font styles to use
Sans Serif
Other font styles liked:
• typewriter

Requirements
Must have
• Visible logo design intergrated into graphics

```html
<!DOCTYPE html>
<html lang="en">
<head>
<meta charset="utf-8">
<title>OK! REELS — Production &amp; Services</title>
<link rel="stylesheet" href="https://fonts.googleapis.com/css2?family=Old+Standard+TT:wght@400;700&family=Libre+Baskerville:ital,wght@0,400;0,700;1,400&display=swap">
<style>
:root{
  --red:#c4202f;
  --blue:#1f5f9c;
  --navy:#0f3c6b;
  --footer:#134a86;
  --band:#141414;
  --ink:#333;
  --muted:#666;
  --white:#fff;
  --rule:#c9cfd6;
}
*{box-sizing:border-box;margin:0;padding:0}
html,body{width:1200px;height:3038px;overflow:hidden;background:var(--white)}
body{font-family:"Libre Baskerville",Georgia,serif;color:var(--ink);position:relative}
.section{position:absolute;left:0;width:1200px}
.center{text-align:center}

/* header */
.site-header{top:0;height:101px}
.brand{position:absolute;left:140px;top:22px;display:flex;align-items:center;gap:12px;font-family:"Old Standard TT",serif;font-weight:700;font-size:40px;color:var(--red);letter-spacing:1px}
.brand-mark{width:14px;height:14px;background:var(--red)}
.main-nav{position:absolute;left:585px;top:35px;display:flex}
.main-nav a{font-family:"Old Standard TT",serif;font-size:19px;color:#333;text-decoration:none;text-transform:uppercase;padding:6px 18px;margin-right:12px}
.main-nav a.is-active{background:var(--red);color:var(--white);border-radius:3px}

/* plain dark edge bands */
.band-edge{position:absolute;left:0;width:100%;height:20px;background:var(--band)}
.band-edge.top{top:0}
.band-edge.bottom{bottom:0}

/* hero */
.hero{top:101px;height:532px}
.hero-photo{position:absolute;inset:0;background:linear-gradient(100deg,#0d2e4b 0%,#1d5a86 45%,#2b6e9b 70%,#174a73 100%)}
.hero-text{position:absolute;left:562px;top:190px;color:var(--white);font-family:"Old Standard TT",serif;text-transform:uppercase;line-height:1}
.hero-text h1{font-size:62px;font-weight:700}
.hero-text .line2{font-size:36px;font-weight:700;margin-top:14px}
.hero-text .line3{font-size:24px;font-weight:700;margin-top:14px}

/* welcome */
.welcome{top:633px;height:405px}
.title-ruled{display:flex;align-items:center;justify-content:center;gap:22px;margin-top:54px}
.title-ruled .rule{width:250px;height:1px;background:var(--rule);position:relative}
.title-ruled .rule::before,.title-ruled .rule::after{content:"";position:absolute;top:-3px;width:7px;height:7px;border-radius:50%;background:var(--rule)}
.title-ruled .rule::before{left:0}.title-ruled .rule::after{right:0}
.section-title{font-family:"Old Standard TT",serif;font-weight:400;color:var(--blue);font-size:40px}
.welcome p{width:930px;margin:30px auto 0;font-size:12.5px;line-height:25px;color:var(--muted);text-align:center}
.btn-outline{position:absolute;left:501px;top:301px;width:198px;height:46px;border:1px solid #d8d8d8;display:flex;font-size:11px;color:#999;text-transform:uppercase;letter-spacing:.5px}
.btn-outline span{flex:1;display:flex;align-items:center;justify-content:center}
.btn-outline i{width:46px;border-left:1px solid #d8d8d8;display:flex;align-items:center;justify-content:center}

/* feature band */
.feature{top:1038px;height:418px;color:var(--white)}
.feature-photo{position:absolute;inset:0;background:linear-gradient(90deg,#2a1d14 0%,#5b412c 40%,#7a583b 55%,#3a281b 100%)}
.feature-body{position:absolute;left:0;right:0;top:95px;text-align:center}
.feature-body h2{font-family:"Old Standard TT",serif;font-weight:400;font-size:54px;margin-top:14px}
.feature-body blockquote{width:830px;margin:22px auto 0;font-style:italic;font-size:17px;line-height:34px}

/* expertise */
.expertise{top:1456px;height:570px}
.expertise .section-title{margin-top:48px}
.tagline{font-style:italic;color:var(--muted);font-size:15px;line-height:28px;margin-top:10px}
.cards{position:absolute;top:177px;left:142px;display:flex;gap:40px}
.card{width:278px;height:322px;background:var(--white);box-shadow:0 2px 10px rgba(0,0,0,.25);padding:18px 18px 0;text-align:left}
.card-photo{height:177px}
.card h3{font-family:"Old Standard TT",serif;font-weight:400;font-size:18px;color:var(--blue);text-transform:uppercase;margin-top:24px}
.card p{font-size:12px;color:var(--muted);margin-top:6px}
.btn-red{display:inline-block;margin-top:14px;background:var(--red);color:var(--white);font-size:12px;padding:7px 14px;border-radius:2px;font-weight:700}

/* testimonials */
.testimonials{top:2026px;height:417px;color:var(--white)}
.testimonials-bg{position:absolute;inset:0;background:radial-gradient(ellipse at 60% 50%,#1f5b8d 0%,#123d66 55%,#0b2a4a 100%)}
.testimonials .section-title{position:relative;color:var(--white);font-size:28px;margin-top:55px}
.quote-box{position:absolute;left:142px;top:134px;width:916px;height:149px;border:1px solid rgba(255,255,255,.45);display:flex;text-align:left}
.avatar{width:157px;height:149px;background:linear-gradient(160deg,#e8d8c8,#b68e70);border:4px solid var(--white)}
.quote-box blockquote{flex:1;padding:22px 26px;font-style:italic;font-size:16px;line-height:30px}
.slider-nav{position:absolute;left:572px;top:337px;display:flex;gap:8px}
.slider-nav span{width:24px;height:24px;border:1px solid rgba(255,255,255,.7);border-radius:50%;display:flex;align-items:center;justify-content:center}

/* newsletter */
.newsletter{top:2443px;height:292px}
.newsletter .section-title{margin-top:40px;font-size:31px}
.newsletter p{width:800px;margin:20px auto 0;font-size:13px;line-height:30px;color:var(--muted)}
.signup{position:absolute;left:413px;top:190px;width:374px;height:46px;background:var(--blue);border-radius:3px;display:flex;align-items:center;padding:0 10px 0 22px;text-align:left}
.signup .field{flex:1;color:#cfe0f0;font-size:11px}
.signup .btn-submit{background:var(--white);color:var(--navy);font-size:15px;padding:4px 12px;border-radius:2px}

/* footer */
.site-footer{top:2735px;height:303px;background:var(--footer);color:var(--white);font-size:12.5px}
.footer-col{position:absolute;top:45px}
.footer-col h4{font-family:"Old Standard TT",serif;font-weight:400;font-size:19px;margin-bottom:18px}
.footer-about{left:142px;width:340px;line-height:24px}
.footer-contact{left:600px;width:260px}
.contact-item{display:flex;gap:14px;align-items:flex-start;line-height:22px;margin-bottom:14px}
.contact-item svg{flex:none;margin-top:3px}
.contact-item .email{color:#f0b24a}
.footer-social{left:927px}
.social-item{display:flex;align-items:center;gap:14px;margin-bottom:18px}
.social-dot{width:32px;height:32px;border-radius:50%;background:var(--white)}
.footer-bottom{position:absolute;left:142px;right:142px;top:240px;border-top:1px solid rgba(255,255,255,.3);padding-top:14px;display:flex;justify-content:space-between;font-size:12px}
.footer-links a{color:var(--white);text-decoration:none}
.footer-links .sep{margin:0 8px;opacity:.7}
</style>
</head>
<body>

<header class="section site-header">
  <div class="brand"><span class="brand-mark"></span>OK! REELS</div>
  <nav class="main-nav">
    <a class="is-active" href="#">Home</a>
    <a href="#">About</a>
    <a href="#">Locations</a>
    <a href="#">Works</a>
  </nav>
</header>

<section class="section hero">
  <div class="hero-photo" role="img" aria-label="Camera operator filming on a city street, blue toned"></div>
  <div class="band-edge top"></div>
  <div class="band-edge bottom"></div>
  <div class="hero-text">
    <h1>Let’s Roll!</h1>
    <div class="line2">Production &amp; Services</div>
    <div class="line3">In Eastern Europe and United States</div>
  </div>
</section>

<section class="section welcome">
  <div class="title-ruled"><span class="rule"></span><h2 class="section-title">Welcome to OK! Reels</h2><span class="rule"></span></div>
  <p>Lorem Ipsum is simply dummy text of the printing and typesetting industry. Lorem Ipsum has been the industry’s standard dummy text ever since the 1500s, when an unknown printer took a galley of type and scrambled it to make a type specimen book. It has survived not only five centuries, but also the leap into electronic typesetting, remaining essentially unchanged. It was popularised in the 1960s with the release of Letraset sheets containing Lorem Ipsum passages, and more recently Lorem Ipsum is simply dummy text of the printing and typesetting industry. Lorem Ipsum has been the industry’s standard dummy text ever since the 1500s, when an unknown printer took a galley of type and scrambled it to make a type specimen book.</p>
  <div class="btn-outline"><span>Learn more</span><i><svg width="10" height="14" viewBox="0 0 10 14"><path d="M2 1l6 6-6 6" fill="none" stroke="#c4202f" stroke-width="2"/></svg></i></div>
</section>

<section class="section feature">
  <div class="feature-photo" role="img" aria-label="Film crew member behind the camera, warm sepia tones"></div>
  <div class="band-edge top"></div>
  <div class="band-edge bottom"></div>
  <div class="feature-body">
    <svg width="44" height="30" viewBox="0 0 44 30" aria-hidden="true"><circle cx="10" cy="7" r="6" fill="#fff"/><circle cx="24" cy="7" r="6" fill="#fff"/><rect x="4" y="14" width="26" height="14" rx="2" fill="#fff"/><path d="M30 19l12-6v16l-12-6z" fill="#fff"/></svg>
    <h2>LOREM IPSUM</h2>
    <blockquote>“Lorem Ipsum is simply dummy text of the printing and typesetting industry. Lorem Ipsum has been the industry’s standard dummy text ever since the 1500s, when unknown printer took a galley of type and scrambled it to make a type specimen book.”</blockquote>
  </div>
</section>

<section class="section expertise center">
  <h2 class="section-title">Our Expertise</h2>
  <p class="tagline">“We define experience as a commitment to learn something new,<br>no matter how much we think we already know.”</p>
  <div class="cards">
    <article class="card">
      <div class="card-photo" role="img" aria-label="Crew filming with a camera rig" style="background:linear-gradient(135deg,#2a2a35,#6b4a58 60%,#b06a70)"></div>
      <h3>Production</h3><p>Russian and English</p><span class="btn-red">View Details</span>
    </article>
    <article class="card">
      <div class="card-photo" role="img" aria-label="Production team gathered around equipment" style="background:linear-gradient(135deg,#3a3028,#8a6a52 55%,#c9a98a)"></div>
      <h3>Production Services</h3><p>Europe &amp; United States of America.</p><span class="btn-red">View Details</span>
    </article>
    <article class="card">
      <div class="card-photo" role="img" aria-label="Editor at a mixing desk in a studio" style="background:linear-gradient(135deg,#4a3a2c,#9a7a5a 55%,#d6c2a8)"></div>
      <h3>Corporate</h3><p>On Site or In Studio</p><span class="btn-red">View Details</span>
    </article>
  </div>
</section>

<section class="section testimonials center">
  <div class="testimonials-bg" role="img" aria-label="Curling film strip over deep blue background"></div>
  <h2 class="section-title">What’s Our Clients Say</h2>
  <div class="quote-box">
    <div class="avatar" role="img" aria-label="Client portrait"></div>
    <blockquote>“Lorem Ipsum is simply dummy text of the printing and typesetting industry. Lorem Ipsum has been the industry’s standard dummy text ever since the 1500s, when an unknown printer took a galley of type and scrambled it to make a type specimen book.”</blockquote>
  </div>
  <div class="slider-nav">
    <span><svg width="8" height="10" viewBox="0 0 8 10"><path d="M6 1L2 5l4 4" fill="none" stroke="#fff" stroke-width="1.5"/></svg></span>
    <span><svg width="8" height="10" viewBox="0 0 8 10"><path d="M2 1l4 4-4 4" fill="none" stroke="#fff" stroke-width="1.5"/></svg></span>
  </div>
</section>

<section class="section newsletter center">
  <h2 class="section-title">Subscribe to Our NewsLetter</h2>
  <p>Lorem Ipsum is simply dummy text of the printing and typesetting industry. Lorem Ipsum has been the industry’s standard dummy text ever since the 1500s, when an unknown printer.</p>
  <div class="signup"><span class="field">Your Email Address...</span><span class="btn-submit">Subscribe</span></div>
</section>

<footer class="section site-footer">
  <div class="footer-col footer-about">
    <h4>OK! Reels</h4>
    <p>Lorem Ipsum is simply dummy text of the printing and typesetting industry. Lorem Ipsum has been all of the industry’s standard dummy text ever since the 1500s, when an unknown printer took a galley of type and scrambled it to make a type and all fo specimen book.</p>
  </div>
  <div class="footer-col footer-contact">
    <h4>Contact Information</h4>
    <div class="contact-item"><svg width="14" height="18" viewBox="0 0 14 18"><path d="M7 0a7 7 0 0 0-7 7c0 5 7 11 7 11s7-6 7-11a7 7 0 0 0-7-7zm0 10a3 3 0 1 1 0-6 3 3 0 0 1 0 6z" fill="#fff"/></svg><span>111 Loreem Ipsum is simply<br>dummy text of the printing.</span></div>
    <div class="contact-item"><svg width="14" height="14" viewBox="0 0 14 14"><path d="M3 0l3 3-2 2c1 2 3 4 5 5l2-2 3 3-2 3C6 14 0 8 0 3z" fill="#fff"/></svg><span>123 1234 5678</span></div>
    <div class="contact-item"><svg width="16" height="12" viewBox="0 0 16 12"><rect x="0.5" y="0.5" width="15" height="11" fill="none" stroke="#fff"/><path d="M1 1l7 6 7-6" fill="none" stroke="#fff"/></svg><span class="email">info@okreels.com</span></div>
  </div>
  <div class="footer-col footer-social">
    <h4>Let’s be Social</h4>
    <div class="social-item"><span class="social-dot"></span>Friendlist</div>
    <div class="social-item"><span class="social-dot"></span>Chirper</div>
    <div class="social-item"><span class="social-dot"></span>Circles+</div>
  </div>
  <div class="footer-bottom">
    <nav class="footer-links"><a href="#">Home</a><span class="sep">|</span><a href="#">About</a><span class="sep">|</span><a href="#">Locations</a><span class="sep">|</span><a href="#">Works</a><span class="sep">|</span><a href="#">Privacy Policy</a></nav>
    <span>Copyright © 2014. OK! Reels All Right reserved.</span>
  </div>
</footer>

</body>
</html>
```